Studio Veralin Flyer September
Plurvanto was very easy to work with. It's seems he is 24/7 in front of the computer to fulfill my wishes. I had already 2 winner design but he was the first one, who offered free changes any time for the next 2 years. Was a pleasure to work with him. Sabine
Zielgruppe
Kosmetikstudio
Aufgabenstellung
Ich wünsche mir einen schönen 2 seitigen A5 Flyer. Der Slogen auf der ersten Seite sollte sein: ERLEBEN SIE INDIVIDUELLE SCHÖNHEIT
Der Flyer sollte einfach sein und zu meinem Logo und Website passen, und natürlich ein Blickfänger sein.
Ich hätte gerne gezeichnete Blumenmuster, ähnlich wie auf den Beispiel-fotos. Auf der ersten Seite möchte ich einen 20 CHF Gutschein für eine Gesichtsbehandlung haben.
Auf der Rückseite die Beschreibung der Behandlung.
Foto von Helene Portas( eine von 2) und die Logos von mir und Helene Portas sind sehr wichtig!
Ich möchte alle Designdateien im originalformat erhalten / sowie entsprechende EPS & PDF.
Besten Dank, Sabine Durmaker

```html
<!DOCTYPE html>
<html lang="de">
<head>
<meta charset="utf-8">
<title>Studio Veralin – Flyer A5</title>
<link href="https://fonts.googleapis.com/css2?family=Source+Sans+3:wght@300;400;600;700&display=swap" rel="stylesheet">
<style>
:root{
  --cyan:#9fd9e3;
  --cyan-deep:#5cc0d3;
  --grey:#a7a29e;
  --grey-dark:#7e7874;
  --text:#8b8582;
  --logo:#9b918c;
  --white:#ffffff;
}
*{margin:0;padding:0;box-sizing:border-box}
html,body{width:1200px;height:848px;overflow:hidden;background:var(--white)}
body{font-family:"Source Sans 3",sans-serif;position:relative}
.page{position:absolute;top:53px;width:505px;height:716px;overflow:hidden;background:var(--white);box-shadow:4px 5px 8px rgba(0,0,0,.18)}
.front{left:70px}
.back{left:626px}

/* front */
.front-bg{position:absolute;inset:0;background:linear-gradient(180deg,#fff 0%,#fff 62%,#d6d2cf 74%,var(--grey) 82%,var(--grey) 100%)}
.portrait{position:absolute;left:0;top:0;width:373px;height:540px;background:radial-gradient(ellipse at 40% 45%,#f3d9c8 0%,#e8c3ad 40%,rgba(240,225,215,.6) 70%,rgba(255,255,255,0) 90%)}
.flower-art{position:absolute;left:230px;top:60px;width:275px;height:540px;background:radial-gradient(ellipse at 60% 45%,rgba(159,217,227,.85) 0%,rgba(159,217,227,.45) 45%,rgba(159,217,227,0) 75%)}
.logo-front{position:absolute;left:282px;top:110px;font-size:27px;font-weight:300;color:var(--logo);letter-spacing:.5px}
.swoosh{position:absolute;left:0;top:0;width:505px;height:716px}
.voucher{position:absolute;left:-4px;top:479px;width:143px;height:130px;border-radius:50%;background:var(--white);border:3px solid var(--cyan);text-align:center;padding-top:20px;color:var(--text);z-index:2}
.voucher .amount{font-size:23px;font-weight:700;line-height:1}
.voucher .label{font-size:22px;font-weight:700;line-height:1.05}
.voucher .sub{font-size:11px;line-height:1.15;color:#6f6a67;margin-top:4px}
.slogan{position:absolute;color:var(--cyan);font-weight:300;line-height:1;white-space:nowrap}
.slogan.l1{top:589px;left:143px}
.slogan.l2{top:632px;left:46px}
.slogan .big{font-size:54px}
.slogan .mid{font-size:38px}
.slogan .small{font-size:30px}
.web-front{position:absolute;left:0;width:505px;top:688px;text-align:center;color:var(--white);font-size:16px;letter-spacing:3px}

/* back */
.hero{position:absolute;left:0;top:0;width:505px;height:193px;background:linear-gradient(90deg,#f2eeea 0%,#ecd7c8 30%,#e9cbb8 45%,#f4ece6 65%,#f7f3f0 100%)}
.partner{position:absolute;right:26px;top:28px;text-align:right;color:#6d6866}
.partner .name{font-size:19px;font-weight:400;letter-spacing:1.5px;line-height:1}
.partner .city{font-size:9px;letter-spacing:1px}
.treatments{position:absolute;left:76px;top:215px;width:352px;color:var(--text)}
.treatment{margin-bottom:17px}
.treatment .head{display:flex;align-items:baseline;color:var(--cyan-deep)}
.treatment .title{font-size:14.5px;font-weight:400;width:177px}
.treatment .dur{font-size:10px;font-weight:600;flex:1}
.treatment .price{font-size:14.5px}
.treatment .steps{font-size:12px;font-weight:600;line-height:1.15;margin:2px 0 5px}
.treatment .desc{font-size:8.7px;line-height:1.28}
.logo-back{position:absolute;left:40px;top:590px;color:var(--logo)}
.logo-back .name{font-size:22px;font-weight:300;letter-spacing:.5px;line-height:1}
.logo-back .url{font-size:6.5px;letter-spacing:1.5px;margin-top:6px}
.booking{position:absolute;left:334px;top:578px;width:158px;height:86px;border-radius:50%;background:var(--white);border:3px solid var(--cyan);text-align:center;color:var(--text);padding-top:10px;z-index:2}
.booking .small{font-size:9.5px;line-height:1.15}
.booking .phone{font-size:15px;line-height:1.1}
.footer{position:absolute;left:0;top:638px;width:505px;height:78px;background:linear-gradient(90deg,#bdb8b5 0%,var(--grey) 30%,var(--grey) 100%);color:var(--white);font-size:9.5px;line-height:1.22}
.footer .contact{position:absolute;left:61px;top:9px}
.footer .contact strong{font-weight:600;font-size:10px}
.footer .contact .role{font-size:6.5px}
.footer .hours{position:absolute;left:189px;top:9px;width:177px}
.footer .hours strong{font-weight:600}
.footer .hours .row{display:flex;justify-content:space-between}
.footer .note{position:absolute;left:382px;top:52px;font-size:6.5px;line-height:1.25}
</style>
</head>
<body>

<section class="page front">
  <div class="front-bg"></div>
  <div class="portrait" role="img" aria-label="Porträtfoto einer Frau mit Händen unter dem Kinn"></div>
  <div class="flower-art" role="img" aria-label="Gezeichnete Blumenranke in Hellblau"></div>
  <div class="logo-front">Studio Veralin</div>
  <svg class="swoosh" viewBox="0 0 505 716" aria-hidden="true">
    <path d="M0 578 C70 568 140 552 230 550 C320 548 400 552 505 626" fill="none" stroke="#9fd9e3" stroke-width="9"/>
  </svg>
  <div class="voucher">
    <div class="amount">20 CHF</div>
    <div class="label">GUTSCHEIN</div>
    <div class="sub">für eine<br>Gesichtsbehandlung</div>
  </div>
  <div class="slogan l1"><span class="big">Erleben</span> <span class="small">sie</span></div>
  <div class="slogan l2"><span class="mid">individuelle</span> <span class="big">Schönheit</span></div>
  <div class="web-front">WWW.STUDIO-VERALIN.CH</div>
</section>

<section class="page back">
  <div class="hero" role="img" aria-label="Foto einer Frau mit weisser Gesichtsmaske in der Hand"></div>
  <div class="partner"><div class="name">HELENE PORTAS</div><div class="city">PARIS</div></div>

  <div class="treatments">
    <article class="treatment">
      <div class="head"><span class="title">SOIN ÉCLAT DORÉ</span><span class="dur">Dauer: 1.45 Std</span><span class="price">149 CHF</span></div>
      <p class="steps">Reinigung, Peeling, Ausreinigung, Augenbrauen in Form bringen, Essencen, Massage, Kollagenmaske, Abschlusspflege.</p>
      <p class="desc">SOIN ÉCLAT DORÉ ist der Champagner unter den Behandlungen von Helene Portas. Sie verleiht ein Optimum an Ausstrahlung und zeigt eine unmittelbare Anti-Aging-Wirkung.<br>Die exklusive Behandlung ist ideal für die Haut ab 40 mit höchsten Ansprüchen.</p>
    </article>
    <article class="treatment">
      <div class="head"><span class="title">SOIN NUAGE</span><span class="dur">Dauer: 1.45 Std</span><span class="price">139 CHF</span></div>
      <p class="steps">Reinigung, Peeling, Ausreinigung, Augenbrauen in Form bringen, Essencen, Massage, Schaummaske, Abschlusspflege</p>
      <p class="desc">Bei der Behandlung SOIN NUAGE dreht sich alles um Wellness und Entspannung. Das Besondere: Wohltuende Massagen begleiten die einzelnen Behandlungsschritte, entspannen die Gesichtszüge, glätten die Haut und vitalisieren das Bindegewebe.</p>
    </article>
    <article class="treatment">
      <div class="head"><span class="title">SOIN LIFT TENDRE</span><span class="dur">Dauer: 1.45 Std</span><span class="price">139 CHF</span></div>
      <p class="steps">Reinigung, Peeling, Ausreinigung, Augenbrauen in Form bringen, Essencen, Massage, Liftingmaske, Abschlusspflege</p>
      <p class="desc">„Lifting“-Effekt, Tiefenwirkung und Entspannung – die festigende Gesichtsbehandlung SOIN LIFT TENDRE sorgt für sofort sicht- und spürbare Resultate. Die Haut wird von innen heraus aufgepolstert, werden Fältchen gemildert und die Gesichtskonturen remodelliert.</p>
    </article>
  </div>

  <div class="logo-back"><div class="name">Studio Veralin</div><div class="url">WWW.STUDIO-VERALIN.CH</div></div>

  <div class="booking">
    <div class="small">Terminvereinbarungen<br>NUR telefonisch</div>
    <div class="phone">076 318 42 90</div>
    <div class="small">Besten Dank</div>
  </div>

  <footer class="footer">
    <div class="contact">
      <strong>Sabine Durmaker</strong><br><span class="role">Kosmetikerin</span><br>
      Lindenweg 12<br>8400 Talwil<br>Telefon: 076-318-4290
    </div>
    <div class="hours">
      <strong>Öffnungszeiten</strong><br>
      Montag geschlossen
      <div class="row"><span>Dienstag/Donnerstag/Freitag:</span><span>9.00-13.00</span></div>
      <div class="row"><span>Mittwoch:</span><span>14.00-18.00</span></div>
      <div class="row"><span>Samstag:</span><span>10.00-16.00</span></div>
    </div>
    <div class="note">andere Termine auch nach<br>Vereinbarung möglich</div>
  </footer>
</section>

</body>
</html>
```